9x12 Business Brochure, 3 fold, for Internet Marketing Company

I'd like to have a brochure designed for my Internet marketing company. I have the content all ready, 10 Internet Marketing Myths, which you can see here: http://www.brightfieldwebgrowth.net/usual-online-promo-fables/. I'm looking for something creative and business to business. The company is all about Internet marketing. I like the "http://" header I use at our website. People like it too and identify with it. Audience is business owners 35 to 55 years old. I use blue at my website. I *think* I would like the cover page (front page) to open with some attention grabbing text, that basically takes most of the front page of the brochure. It would probably say: "I Can Help You Get BETTER RESULTS from Your Website, More Traffic, TOP RANKINGS at Zorvix, More Leads and MORE SALES. But first you'll have to avoid these common Internet marketing myths..." The inside pages would have the content from above (the 10 myths). The back page would have testimonials that I can provide. And the inside folded in page (or what I call the inside folded in page) would have a list of services. I think I want the dimensions 12x9 which is a larger sized, three-fold brochure.

Target Market(s)

I use this brochure to send to business owners and managers to show them I know what I'm talking about and and expert. See attachment for content.

Industry/Entity Type

Marketing

Requirements
Should not have
• No clipart. Probably not illustrations. Photos. The "http://" used at the site is something people "connect" with and get that this is about Internet marketing.

```html
<!DOCTYPE html>
<html lang="en">
<head>
<meta charset="utf-8">
<title>Brochure Layout – Dana Merrow Consulting</title>
<link href="https://fonts.googleapis.com/css2?family=Arvo:wght@400;700&family=Roboto+Slab:wght@400;700&family=Roboto+Condensed:wght@400;700&family=Open+Sans:wght@400;600&display=swap" rel="stylesheet">
<style>
:root{
  --teal:#1fa9c9;
  --teal-light:#5fcbe2;
  --teal-pale:#b9e7f1;
  --navy:#1c4a84;
  --navy-dark:#163a6b;
  --bubble-border:#2d6ea9;
  --orange:#e59a1c;
  --ink:#333;
  --grey-text:#7a7a7a;
  --panel-edge:#dcdcdc;
}
*{margin:0;padding:0;box-sizing:border-box}
html,body{width:1200px;height:896px;overflow:hidden;background:#fff}
body{position:relative;font-family:"Roboto Slab",serif;color:var(--ink)}
.abs{position:absolute}

.view-label{position:absolute;font-family:"Roboto Slab",serif;font-size:12px;color:#777}

/* back spread */
.back-panel{position:absolute;top:37px;height:435px;width:195px;
  background:linear-gradient(90deg,#e9e9e9 0%,#fafafa 40%,#f3f3f3 100%)}
.back-panel.right{background:linear-gradient(90deg,#f3f3f3 0%,#fafafa 60%,#e1e1e1 100%)}
.section-title{position:absolute;left:61px;top:64px;font-family:"Roboto Slab",serif;font-size:11px;color:var(--grey-text)}
.map-area{position:absolute;left:22px;top:148px;width:366px;height:190px;
  background:radial-gradient(ellipse at 50% 50%,rgba(31,169,201,.55) 0%,rgba(31,169,201,.25) 55%,rgba(31,169,201,0) 75%)}
.bubble{position:absolute;background:#fff;border:2px solid var(--bubble-border);border-radius:6px;padding:3px 5px;
  font-family:"Roboto Slab",serif;font-size:4.6px;line-height:5.6px;color:#333;text-align:justify}
.bubble h4{font-family:"Arvo",serif;font-size:5.4px;color:var(--orange);margin-bottom:1px}
.bubble.soft{background:rgba(255,255,255,.55);border-color:transparent}
.pointer{position:absolute}
.back-contact{position:absolute;left:195px;width:194px;top:409px;text-align:center;
  font-family:"Roboto Slab",serif;font-weight:700;font-size:5.8px;line-height:7.4px;color:var(--navy)}

/* front */
.front{position:absolute;left:389px;top:37px;width:193px;height:435px;overflow:hidden;
  background:linear-gradient(180deg,var(--teal) 0%,#2fb5d2 35%,#7fd3e6 58%,#3cb6d3 78%,var(--teal) 100%)}
.front-map{position:absolute;left:0;top:0;width:193px;height:140px;
  background:radial-gradient(ellipse at 50% 45%,rgba(255,255,255,.7) 0%,rgba(255,255,255,.25) 55%,rgba(255,255,255,0) 80%)}
.headline{position:absolute;left:0;width:193px;top:180px;text-align:center;
  font-family:"Roboto Condensed",sans-serif;font-weight:700;color:var(--navy);line-height:20px;font-size:14.5px}
.headline .big{font-size:17px}
.front-sub{position:absolute;left:0;width:193px;top:314px;text-align:center;
  font-family:"Open Sans",sans-serif;font-size:6px;line-height:8.5px;color:var(--navy)}
.front-contact{position:absolute;left:0;width:193px;top:349px;text-align:center;
  font-family:"Open Sans",sans-serif;font-size:6px;line-height:8.5px;color:var(--navy)}
.arrows{position:absolute;left:0;top:360px}

/* inside spread */
.inside-panel{position:absolute;top:354px;height:436px;width:194px;overflow:hidden}
.inside-panel.p1{left:592px;width:204px;background:linear-gradient(90deg,#fff 0%,#fff 82%,#e4e4e4 100%)}
.inside-panel.p2{left:796px;width:184px;background:linear-gradient(90deg,#f6f6f6 0%,#fff 30%,#fff 80%,#e3e3e3 100%)}
.inside-panel.p3{left:980px;width:194px;background:linear-gradient(90deg,#f2f2f2 0%,#fff 40%,#ececec 100%)}
.myths-header{position:absolute;left:0;top:0}
.myths-title{position:absolute;left:22px;top:27px;font-family:"Arvo",serif;font-weight:700;font-size:10.5px;line-height:14px;color:#fff}
.myth-copy{position:absolute;font-family:"Roboto Slab",serif;font-size:4.9px;line-height:6.4px;color:#333;text-align:justify}
.myth-copy h3{font-family:"Arvo",serif;font-weight:700;font-size:5.3px;line-height:6.6px;color:#222}
.myth-copy p{margin-bottom:6px}
.services-box{position:absolute;left:12px;top:23px;width:168px;height:390px;background:var(--teal);border-radius:7px}
.services-title{position:absolute;left:0;width:168px;top:21px;text-align:center;
  font-family:"Arvo",serif;font-weight:700;font-size:6.8px;color:#fff}
.services-list{position:absolute;left:0;width:168px;top:44px;list-style:none;text-align:center;
  font-family:"Arvo",serif;font-weight:700;font-size:5.2px;line-height:14.3px;color:#fff}
.quote-icon{position:absolute;left:5px;top:302px}
.services-quote{position:absolute;left:30px;top:342px;width:122px;text-align:center;
  font-family:"Arvo",serif;font-weight:700;font-size:5.2px;line-height:6.8px;color:#fff}
</style>
</head>
<body>

<!-- BACK -->
<section class="back-spread">
  <div class="back-panel" style="left:0"></div>
  <div class="back-panel right" style="left:195px"></div>
  <h2 class="section-title">Success Stories</h2>
  <div class="map-area" role="img" aria-label="World map in teal spreading across the back panels"></div>

  <svg class="pointer" style="left:0;top:0" width="389" height="472" aria-hidden="true">
    <g fill="#fff" stroke="#2d6ea9" stroke-width="1.5">
      <polygon points="128,157 138,157 146,178"/>
      <polygon points="110,261 122,261 120,283"/>
      <polygon points="108,295 120,295 100,270"/>
      <polygon points="268,159 280,159 270,185"/>
      <polygon points="226,294 238,294 224,260"/>
    </g>
  </svg>

  <div class="bubble" style="left:68px;top:99px;width:108px;height:59px">
    <h4>Zorvix Rankings</h4>
    "... we have spent over a year trying to get onto page one at Zorvix. I has been very frustrating and we've wasted a lot of time and money. Dana explained everything very clearly and we did everything he told us. 90 days later we're now showing up on the first page of Zorvix!"
  </div>
  <div class="bubble" style="left:25px;top:187px;width:127px;height:75px">
    <h4>Website Design</h4>
    "We needed a new website that properly reflected our company and the products and services we sell. We started getting more leads within 72 hours of launching the new site Dana and his team designed for us. We're also getting better results from our Zorvix AdLines pay-per-click advertising and more of those clicks are turning into inquiries!"
  </div>
  <div class="bubble" style="left:56px;top:294px;width:114px;height:55px">
    <h4>More to Come</h4>
    Lorem ipsum dolor sit amet, consectetur adipiscing elit. Suspendisse justo velit, auctor ut pulvinar a, egestas non urna. Suspendisse potenti. Sed ut pellentesque dolor. Vivamus sed nibh nisl. Nunc tortor tellus, facilisis eget pretium vitae, porttitor quis libero.
  </div>
  <div class="bubble" style="left:234px;top:108px;width:115px;height:52px">
    <h4>More to Come</h4>
    Lorem ipsum dolor sit amet, consectetur adipiscing elit. Suspendisse justo velit, auctor ut pulvinar a, egestas non urna. Suspendisse potenti. Sed ut pellentesque dolor. Vivamus sed nibh nisl. Nunc tortor tellus, facilisis eget pretium vitae, porttitor quis libero.
  </div>
  <div class="bubble soft" style="left:265px;top:204px;width:114px;height:48px">
    <h4>More to Come</h4>
    Lorem ipsum dolor sit amet, consectetur adipiscing elit. Suspendisse justo velit, auctor ut pulvinar a, egestas non urna. Suspendisse potenti. Sed ut pellentesque dolor. Vivamus sed nibh nisl. Nunc tortor tellus, facilisis eget pretium vitae, porttitor quis libero.
  </div>
  <div class="bubble" style="left:207px;top:293px;width:115px;height:55px">
    <h4>More to Come</h4>
    Lorem ipsum dolor sit amet, consectetur adipiscing elit. Suspendisse justo velit, auctor ut pulvinar a, egestas non urna. Suspendisse potenti. Sed ut pellentesque dolor. Vivamus sed nibh nisl. Nunc tortor tellus, facilisis eget pretium vitae, porttitor quis libero.
  </div>

  <div class="back-contact">Dana Merrow<br>Dana Merrow Consulting (.com)<br>(555) 014-2280</div>
</section>

<!-- FRONT -->
<section class="front">
  <div class="front-map" role="img" aria-label="White world map over a bright blue sky"></div>
  <h1 class="headline">
    I Can Help You Get<br>
    <span class="big">BETTER RESULTS</span> from<br>
    Your Website, More Traffic,<br>
    <span class="big">TOP RANKINGS</span> with<br>
    Zorvix, More Inquiries,<br>
    and <span class="big">MORE SALES</span>
  </h1>
  <p class="front-sub">But first you'll need to avoid these<br>Common Internet Marketing Myths...</p>
  <p class="front-contact">Dana Merrow Consulting (.com)<br>(555) 014-2280</p>
  <svg class="arrows" width="193" height="75" aria-hidden="true">
    <polygon points="6,50 30,30 54,50 40,50 40,75 20,75 20,50" fill="#a6e0ec"/>
    <polygon points="48,28 80,4 112,28 92,28 92,75 68,75 68,28" fill="#2f6aa3"/>
    <polygon points="96,50 120,30 144,50 128,50 128,75 112,75 112,50" fill="#1d4c86"/>
    <polygon points="138,30 165,6 192,30 176,30 176,75 154,75 154,30" fill="#b8e8f2"/>
  </svg>
</section>

<!-- INSIDE -->
<section class="inside-panel p1">
  <svg class="myths-header" width="204" height="110" aria-hidden="true">
    <path d="M0,0 H196 C190,60 150,96 100,98 C55,100 20,80 0,55 Z" fill="#1fa9c9"/>
    <path d="M0,55 C20,80 55,100 100,98 C150,96 190,60 196,0 L200,0 C196,66 152,104 100,104 C52,104 18,86 0,64 Z" fill="#e6f6fa"/>
  </svg>
  <h2 class="myths-title">Common Internet<br>Marketing Myths</h2>
  <div class="myth-copy" style="left:11px;top:110px;width:184px;height:320px;overflow:hidden">
    <h3>Myth #1: If You Build It They Will Come</h3>
    <p>Building a website is no guarantee of online success. If you build it, don't assume people will find it. This is a guaranteed losing strategy. For your Internet marketing to succeed your website will need quality traffic (i.e. visitor sessions) and then convert those visitors into phone calls and online inquiries.</p>
    <h3>Myth #2: Search Engines Are All You'll Need</h3>
    <p>It is a very common misconception, and costly mistake, to think that search engines and organic search engine positioning is all you need for online success. While a top ranked website is a very valuable asset, and it can drive a lot of qualified traffic to your website, it can take months, or years, to achieve that positioning — if you can get it at all. You'll need a multi-pronged approach to building traffic, including buying advertising, pay-per-click advertising (PPC), integration of your offline marketing with your online marketing, blogging, social media, and of course, search engine optimization (SEO).</p>
    <h3>Myth #3: All Traffic Is Good</h3>
    <p>Not true! To get real results from your website, inquiries, phone calls and sales, you'll need to find and attract QUALIFIED traffic – people who are actually getting started and who are ready to purchase your products and services.</p>
    <h3>Myth #4: Hits Are A Good Measure Of Success</h3>
    <p>Wrong! If you are measuring "hits" you're not even in the game. A "hit" is a technical term that describes activity on a hosting server. Unfortunately, most webmasters use this term casually and it is interpreted to mean you have lots of traffic. Hits are not real people. Real people who visit your website are logged as "visitor sessions."</p>
    <h3>Myth #5: You Can Do This All Yourself</h3>
    <p style="margin-bottom:1px">If you are in any competitive category of products or services, or in a geographically competitive marketplace, the chances that you can build a website, develop the traffic, and manage your ongoing online marketing ALL BY YOURSELF are less than one in ten. Put another way, DIY has a 90% chance of FAILURE.</p>
    <h3>Myth #6: It's Easy To Get Traffic From Search Engines</h3>
  </div>
</section>

<section class="inside-panel p2">
  <div class="myth-copy" style="left:6px;top:12px;width:172px">
    <p>In today's competitive marketplace it is more difficult than ever to get top ranking with Zorvix, Yarvo, or Bindle. It is very likely going to take six to twelve months to see your website achieve a top ranked position for any competitive keyword/keyword phrase that people are searching for – and that's only if you have SEO expertise. If your website is new it will take longer.</p>
    <h3>Myth #7: Submitting Your Website To Search Engines Actually Works</h3>
    <p>Not true! Submitting your website to the search engines each month is USELESS. Companies or individuals that provide this service will gladly take your money and it is unlikely you'll see any benefit. The best way to get your website indexed in the search engines is for them to find your website link at another regularly crawled, thematically-similar website. A Zorvix Sitemap will also help you get your website indexed and crawled more effectively.</p>
    <h3>Myth #8: Search Engine Optimization Is Easy</h3>
    <p>Search engine optimization is not difficult but there is a lot to it. There are dozens of different variables that must be perfectly managed. Each of these falls into one of two categories: "on-page" variables or "off-page" variables. Add to this hundreds of so-called "experts" and their advice (which is incorrect, incomplete, or misleading), and it's pretty hard to call the search engine optimization process easy. Getting top ranked is even more challenging when a competitor has hired a reputable SEO expert to help them with their website and Internet marketing strategy.</p>
    <h3>Myth #9: Meta-Tags Are The Key To A Top Ranked Website</h3>
    <p>Meta-tags are specific lines of programming code that appear behind-the-scenes at your website. Search engines see them but your visitors do not. Search engines use meta-tags as one of the factors in determining page relevancy. Zorvix's algorithm tries to show the most relevant pages for a search on a search engine results page (SERP). Meta-tags are still important, but only one of more than two dozen factors related to the overall search engine optimization of your website.</p>
    <h3>Myth #10: Your Webmaster / Programmer Can Help You With Your Internet Marketing</h3>
    <p>Graphics design, programming code, and page layout are very different from Internet marketing. In most cases, (90% of the time) a webmaster / programmer will not be able to give you the appropriate advice or support to effectively promote and market your website online.</p>
  </div>
</section>

<section class="inside-panel p3">
  <div class="services-box">
    <h2 class="services-title">Services &amp; Expertise</h2>
    <ul class="services-list">
      <li>Internet Strategy Development</li>
      <li>Custom Website Design</li>
      <li>Blog Design &amp; Support</li>
      <li>Online Marketing Copywriting</li>
      <li>Social Media Marketing</li>
      <li>Search Engine Optimization (SEO)</li>
      <li>Conversion Optimization</li>
      <li>Content Marketing Management</li>
      <li>Using Friendlo for Business</li>
      <li>Zorvix+, Cliptube, Pinboardly</li>
      <li>Email Marketing &amp; Production</li>
      <li>Inquiry and Lead Development</li>
      <li>Zorvix AdLines Pay-Per-Click</li>
      <li>Zorvix Local Places (maps)</li>
      <li>E-Commerce Development</li>
      <li>High-Performance Hosting</li>
      <li>Security &amp; Contingency Planning</li>
      <li>One-on-One or Group Training</li>
    </ul>
    <svg class="quote-icon" width="30" height="42" aria-hidden="true">
      <circle cx="17" cy="16" r="9" fill="#e8f6fa" stroke="#555" stroke-width="2.5"/>
      <line x1="11" y1="23" x2="3" y2="37" stroke="#444" stroke-width="4" stroke-linecap="round"/>
      <circle cx="17" cy="4" r="2.5" fill="#7cc242"/>
    </svg>
    <p class="services-quote">"If you think it's expensive to hire an expert,<br>wait until you hire an amateur."</p>
  </div>
</section>

<span class="view-label" style="left:173px;top:491px">Back</span>
<span class="view-label" style="left:459px;top:491px">Front</span>
<span class="view-label" style="left:865px;top:805px">Inside</span>

</body>
</html>
```